Harbor of Embers How a Quiet Mill Town Found Its Second Song.

This compelling story deserves a great cover which conveys transformation. As a pastor, I started a church in the financial district of Atlanta. What began as a typical "church plant" became an adventure in risk, creativity, and the building was a beautiful metaphor of transformation as we took a closed down strip club and turned it into a church venue. Our group learned many lessons about accepting people from all sorts of backgrounds, and about seeing God's power at work. I envision a cover which communicates transformation, perhaps using darkness and light, or maybe using the Rivet Lounge building being painted. It was a solid black building (with gold trim) and we painted it white, with a blue logo of the church name. I need book cover, spine, and back, along with whatever is needed for Brindlemart to accept it for their site.

```html
<!DOCTYPE html>
<html lang="en">
<head>
<meta charset="utf-8">
<title>Harbor of Embers – Book Cover</title>
<link href="https://fonts.googleapis.com/css2?family=Cinzel:wght@400;500;600&family=Roboto+Condensed:wght@700&display=swap" rel="stylesheet">
<style>
  :root {
    --stage: #222222;
    --cover: #050505;
    --gold: #c9b68a;
    --cream: #f4ecd8;
    --white: #ffffff;
    --pew: #5a3422;
    --beam-edge: #3a3120;
    --beam-mid: #e9dcb8;
  }
  * { margin: 0; padding: 0; box-sizing: border-box; }
  html, body {
    width: 1200px; height: 1200px; overflow: hidden;
    background: var(--stage);
  }
  .cover {
    position: absolute; left: 208px; top: 12px;
    width: 784px; height: 1176px;
    background: var(--cover);
    overflow: hidden;
  }
  .light-art {
    position: absolute; left: 190px; top: 0;
    width: 190px; height: 960px;
    background: linear-gradient(90deg, var(--beam-edge) 0%, var(--beam-mid) 50%, var(--beam-edge) 100%);
  }
  .pew {
    position: absolute; left: 236px; top: 822px;
    width: 90px; height: 90px;
    background: var(--pew);
  }
  .title {
    position: absolute; inset: 0;
    font-family: "Cinzel", "Trajan Pro", serif;
    font-weight: 400;
  }
  .title span { position: absolute; line-height: 1; white-space: nowrap; }
  .title-outline {
    left: 0; right: 0; top: 262px;
    text-align: center;
    font-size: 154px;
    color: transparent;
    -webkit-text-stroke: 2px var(--gold);
  }
  .title-small {
    left: 286px; top: 452px;
    font-size: 86px;
    color: var(--gold);
  }
  .title-solid {
    left: 0; right: 0; top: 577px;
    text-align: center;
    font-size: 170px; font-weight: 500;
    background: linear-gradient(180deg, var(--white) 0%, var(--cream) 45%, var(--gold) 100%);
    -webkit-background-clip: text; background-clip: text;
    color: transparent;
  }
  .subtitle {
    position: absolute; left: 410px; top: 772px;
    font-family: "Roboto Condensed", "Arial Narrow", sans-serif;
    font-weight: 700; font-size: 34px; line-height: 44px;
    color: var(--white);
  }
  .subtitle-accent { color: var(--gold); }
  .author {
    position: absolute; left: 0; right: 0; top: 1030px;
    font-family: "Cinzel", "Trajan Pro", serif;
    font-size: 56px; font-weight: 500;
    color: var(--white); text-align: center;
  }
</style>
</head>
<body>
  <main class="cover">
    <div class="light-art" role="img" aria-label="Illustrated shaft of golden light falling from above and glowing on the floor"></div>
    <div class="pew" role="img" aria-label="Illustration of a wooden church pew standing in the light"></div>

    <h1 class="title">
      <span class="title-outline">HARBOR</span>
      <span class="title-small">OF</span>
      <span class="title-solid">EMBERS</span>
    </h1>

    <p class="subtitle">
      How a Quiet Mill<br>
      Town Found Its<br>
      <span class="subtitle-accent">Second Song</span>
    </p>

    <p class="author">Author Name</p>
  </main>
</body>
</html>
```